Concrete Finishing business needs new business card and a logo design

We are a family owned and operated, concrete finishing business. 2020 marks our 33 rd year in business. We operate under Harold P. Mercer and Sons Concrete Contractors Ltd. Harold P was my father and founder of the company. We usually shorten the name and use H P Mercer & Sons Ltd. Most people in the Concrete Finishing industry tend to know us by our last name 'Mercer' . in honour of our father, we would still like to have his name on the cards and logo but are open to shortening it to H.P (maybe in a small font with the H on top of the P ) and focusing more on the "Mercer & Sons."....Or maybe something with just the initials HPM...or if you could use the "P" and somehow incorporate an artistic drawing/shape of a 'power trowel' (what we use apply a smooth finish to the concrete with) but still visually see that its a P, would be cool. Would like to see designs using Black with silver or grey lettering but are open to other ideas. Seen a business card online with the front of the business card looking like concrete and with just the word CONCRETE on it... On the back was the company name , address and contact info of the company....looked really good! i clicked doubled sided in case of something like that but we are open to just single sided as well. After viewing some of the designs, maybe a pop of colour would be nice ... open to any ideas and colours.😊

Target Market(s)

Construction

```html
<!DOCTYPE html>
<html lang="en">
<head>
<meta charset="utf-8">
<title>H P Mercer &amp; Sons Ltd. – Business Card</title>
<link href="https://fonts.googleapis.com/css2?family=Arimo:wght@400;700&family=Oswald:wght@600&display=swap" rel="stylesheet">
<style>
  :root {
    --stage: #101010;
    --card: #1b1b1b;
    --silver: #d8d8d6;
    --grey: #b4b4b2;
    --rule: #6a6a6a;
  }
  * { margin: 0; padding: 0; box-sizing: border-box; }
  html, body { width: 1200px; height: 900px; overflow: hidden; background: var(--stage); }
  .stage {
    width: 1200px; height: 900px;
    display: flex; flex-direction: column; align-items: center; justify-content: center; gap: 34px;
  }
  .card {
    width: 700px; height: 400px;
    background: var(--card);
    position: relative;
    box-shadow: 0 10px 30px rgba(0,0,0,.6);
  }
  /* front */
  .card-front { display: flex; align-items: center; justify-content: center; }
  .brand { display: flex; align-items: center; gap: 22px; }
  .brand-square { width: 64px; height: 64px; background: var(--silver); }
  .brand-name {
    font-family: "Arimo", Arial, sans-serif; font-weight: 700;
    font-size: 46px; line-height: 1.1; letter-spacing: 2px;
    color: var(--silver); text-transform: uppercase;
  }
  /* back */
  .person {
    position: absolute; left: 150px; top: 150px; text-align: right; width: 200px;
  }
  .person-name {
    font-family: "Oswald", sans-serif; font-weight: 600; font-size: 27px;
    color: #fff; text-transform: uppercase; letter-spacing: .5px; line-height: 1.1;
  }
  .person-role {
    font-family: "Arimo", Arial, sans-serif; font-size: 19px; color: var(--grey); margin-top: 2px;
  }
  .divider {
    position: absolute; left: 382px; top: 140px; width: 1px; height: 118px; background: var(--rule);
  }
  .contacts {
    position: absolute; left: 402px; top: 146px; list-style: none;
    font-family: "Arimo", Arial, sans-serif; font-size: 20px; color: var(--grey);
  }
  .contacts li { display: flex; align-items: center; gap: 10px; height: 26px; }
  .contacts svg { width: 18px; height: 18px; fill: none; stroke: var(--grey); stroke-width: 1.6; flex: none; }
  .address {
    position: absolute; left: 0; right: 0; bottom: 62px; text-align: center;
    font-family: "Arimo", Arial, sans-serif; font-size: 21px; color: var(--silver); letter-spacing: .3px;
  }
</style>
</head>
<body>
<main class="stage">
  <section class="card card-front" aria-label="Card front">
    <div class="brand">
      <span class="brand-square" aria-hidden="true"></span>
      <span class="brand-name">H.P Mercer<br>and Sons Ltd</span>
    </div>
  </section>

  <section class="card card-back" aria-label="Card back">
    <div class="person">
      <p class="person-name">Daniel Walsh</p>
      <p class="person-role">Managing Director</p>
    </div>
    <span class="divider" aria-hidden="true"></span>
    <ul class="contacts">
      <li>
        <svg viewBox="0 0 18 18" aria-hidden="true"><rect x="5" y="1.5" width="8" height="15" rx="1.5"/><line x1="8" y1="14" x2="10" y2="14"/></svg>
        (709)555-0142
      </li>
      <li>
        <svg viewBox="0 0 18 18" aria-hidden="true"><path d="M4 2l3 3-1.5 2c1 2 2.5 3.5 4.5 4.5L12 10l3 3-2 2.5C7.5 15 3 10.5 2.5 5z"/></svg>
        (709)555-0187
      </li>
      <li>
        <svg viewBox="0 0 18 18" aria-hidden="true"><rect x="2" y="7" width="14" height="7" rx="1"/><rect x="5" y="2.5" width="8" height="4.5"/><rect x="5" y="11" width="8" height="4.5"/></svg>
        (709)555-0163
      </li>
      <li>
        <svg viewBox="0 0 18 18" aria-hidden="true"><rect x="2" y="4" width="14" height="10" rx="1"/><path d="M2 4l7 6 7-6"/></svg>
        office@hpmercer.example
      </li>
    </ul>
    <p class="address">P.O.Box 41, Site 9, RR#2 Harbour Point, NL A0L 2B0</p>
  </section>
</main>
</body>
</html>
```